Private Security Company Business Card and Logo Design

Looking for a modern conservative business card design for our new private security company Harbor Ridge Guard Co., Inc. or HRGC for short.
Private Security Services. The current logo we have is not very good and honestly would like a sharp logo for the card instead of using the one we have now. Open to ideas. I am easy just looking for something nicer then what I can personally design on cardmillo. I searched on zintoo for Security Company business cards went to images and found some nice designs that were made here.

Target Market(s)

Security Services

Industry/Entity Type

Business

Contact Information for Business Card

Harbor Ridge Guard Co., Inc.
President, cell,office,fax,email, website,
Logo etc, whatever is needed for a standard business card
Can provide personal Information later.

Colors
0556a4
ffffff
474747

Requirements
Must have
• Modern but conservative,
Nice to have
• color choices
• Blue, white, Grey

```html
<!DOCTYPE html>
<html lang="en">
<head>
<meta charset="utf-8">
<title>Harbor Ridge Guard Co., Inc. — Business Card</title>
<link rel="stylesheet" href="https://fonts.googleapis.com/css2?family=Questrial&display=swap">
<style>
  :root {
    --brand-blue: #0556a4;
    --blue-light: #2a78c9;
    --blue-dark: #0a3f78;
    --white: #ffffff;
    --paper: #f3f3f3;
    --grey: #474747;
    --charcoal: #3a3a3c;
    --band: #1f1f20;
    --text-light: #e8e8e8;
    --stage: #e4e4e4;
  }
  * { box-sizing: border-box; margin: 0; padding: 0; }
  html, body { width: 1200px; height: 727px; overflow: hidden; }
  body {
    background: var(--stage);
    font-family: "Questrial", "Century Gothic", sans-serif;
    position: relative;
  }
  .card {
    position: absolute;
    top: 212px;
    width: 530px;
    height: 303px;
    overflow: hidden;
    box-shadow: 0 6px 18px rgba(0,0,0,0.18);
  }
  .card-back { left: 50px; background: var(--charcoal); }
  .card-front { left: 620px; background: var(--charcoal); }

  .wordmark {
    display: flex;
    align-items: center;
    gap: 10px;
    color: var(--brand-blue);
    font-weight: 400;
    letter-spacing: 0.18em;
    white-space: nowrap;
  }
  .wordmark-square { background: var(--brand-blue); display: block; flex: none; }

  .card-back .wordmark {
    position: absolute; left: 50%; top: 50%;
    transform: translate(-50%, -50%);
    font-size: 64px;
  }
  .card-back .wordmark-square { width: 34px; height: 34px; }

  .front-top {
    position: absolute; left: 0; top: 0; width: 100%; height: 170px;
    background: var(--paper);
  }
  .card-front .wordmark {
    position: absolute; left: 340px; top: 52px;
    transform: translateX(-50%);
    font-size: 34px;
  }
  .card-front .wordmark-square { width: 18px; height: 18px; }

  .ribbon { position: absolute; left: 0; top: 0; }

  .name-block {
    position: absolute; left: 230px; width: 220px; top: 150px;
    text-align: center;
  }
  .name { color: var(--white); font-size: 26px; line-height: 30px; letter-spacing: 0.02em; }
  .title { color: var(--brand-blue); font-size: 13px; line-height: 16px; }

  .contacts {
    position: absolute; left: 50px; top: 226px;
    display: grid;
    grid-template-columns: 140px 150px 120px;
    row-gap: 14px;
    color: var(--text-light); font-size: 13px; line-height: 16px;
  }
  .contact { display: flex; align-items: center; gap: 8px; white-space: nowrap; }
  .contact svg { width: 12px; height: 12px; fill: var(--brand-blue); flex: none; }
</style>
</head>
<body>
  <section class="card card-back" aria-label="Card back">
    <div class="wordmark"><span class="wordmark-square"></span>HRGC</div>
  </section>

  <section class="card card-front" aria-label="Card front">
    <div class="front-top"></div>

    <svg class="ribbon" width="530" height="303" viewBox="0 0 530 303" aria-hidden="true">
      <polygon points="0,140 40,130 60,148 0,175" fill="var(--brand-blue)"/>
      <polygon points="40,130 70,136 60,148" fill="var(--blue-light)"/>
      <polygon points="0,175 60,148 50,204 0,204" fill="var(--blue-dark)"/>
      <rect x="45" y="148" width="445" height="54" fill="var(--band)"/>
      <polygon points="490,148 530,142 530,212 500,206" fill="var(--brand-blue)"/>
      <polygon points="478,202 490,148 500,206" fill="var(--blue-dark)"/>
    </svg>

    <div class="wordmark"><span class="wordmark-square"></span>HRGC</div>

    <div class="name-block">
      <div class="name">Your Name</div>
      <div class="title">President</div>
    </div>

    <div class="contacts">
      <div class="contact">
        <svg viewBox="0 0 12 12"><rect x="3" y="0" width="6" height="12" rx="1"/></svg>000 000 0000
      </div>
      <div class="contact">
        <svg viewBox="0 0 12 12"><path d="M1 4 Q6 0 11 4 L10 6 L8 5 L8 4 Q6 3 4 4 L4 5 L2 6 Z"/><rect x="3" y="7" width="6" height="4"/></svg>000 000 0000
      </div>
      <div class="contact">
        <svg viewBox="0 0 12 12"><rect x="3" y="1" width="6" height="3"/><rect x="1" y="4" width="10" height="5" rx="1"/><rect x="3" y="8" width="6" height="3"/></svg>000 000 0000
      </div>
      <div class="contact">
        <svg viewBox="0 0 12 12"><rect x="0" y="2" width="12" height="8"/></svg>youremail@xyz.com
      </div>
      <div class="contact">
        <svg viewBox="0 0 12 12"><circle cx="6" cy="6" r="5.5"/></svg>www.yourweb.com
      </div>
    </div>
  </section>
</body>
</html>
```